I need new business cards designed

I would like to get some new designs on business cards. I will upload my logo for reference. The business cards that were designed for me a few months ago were too difficult for the print companies to work with. My company is Brivoldex.com LLC. It is an art company that sells painting and expression cards online.

```html
<!DOCTYPE html>
<html lang="en">
<head>
<meta charset="utf-8">
<title>Brivoldex.com LLC — Business Cards</title>
<link rel="stylesheet" href="https://fonts.googleapis.com/css2?family=Montserrat:wght@400;500;600&family=Open+Sans:wght@400&display=swap">
<style>
  :root {
    --navy: #22296b;
    --sky: #0ea0db;
    --green: #8dc63f;
    --orange: #f7941d;
    --red: #ed1c24;
    --white: #ffffff;
    --backdrop: #3b3b3d;
    --rule: rgba(255,255,255,0.55);
  }
  * { box-sizing: border-box; margin: 0; padding: 0; }
  html, body {
    width: 1200px; height: 1200px; overflow: hidden;
    background: var(--backdrop);
  }
  .canvas { position: relative; width: 1200px; height: 1200px; }

  .card {
    position: absolute; left: 170px; width: 860px; height: 491px;
    border-radius: 28px; overflow: hidden;
    box-shadow: 0 18px 40px rgba(0,0,0,0.45);
  }
  .card--front { top: 60px; background: var(--white); }
  .card--back { top: 630px; background: var(--navy); }

  .color-stripe { position: absolute; left: 0; width: 100%; display: flex; }
  .color-stripe span:nth-child(1) { flex: 33; background: var(--sky); }
  .color-stripe span:nth-child(2) { flex: 22; background: var(--green); }
  .color-stripe span:nth-child(3) { flex: 21; background: var(--orange); }
  .color-stripe span:nth-child(4) { flex: 24; background: var(--red); }
  .card--front .color-stripe { top: 232px; height: 9px; }
  .card--back .color-stripe { bottom: 0; height: 16px; }

  .front-panel {
    position: absolute; left: 0; top: 241px; width: 100%; bottom: 0;
    background: var(--navy);
  }

  .brand { position: absolute; display: flex; align-items: center; }
  .brand-mark { background: var(--sky); flex: none; }
  .brand-name {
    font-family: "Open Sans", sans-serif; font-weight: 400;
    letter-spacing: 0.5px; line-height: 1; white-space: nowrap;
  }

  .card--front .brand { left: 140px; top: 74px; gap: 24px; }
  .card--front .brand-mark { width: 84px; height: 84px; }
  .card--front .brand-name { font-size: 62px; color: var(--navy); }

  .card--back .brand { left: 120px; top: 178px; gap: 30px; }
  .card--back .brand-mark { width: 118px; height: 118px; }
  .card--back .brand-name { font-size: 80px; color: var(--white); }

  .person {
    position: absolute; left: 62px; top: 34px; width: 330px;
    font-family: "Montserrat", sans-serif; color: var(--white);
  }
  .person-name { font-size: 38px; font-weight: 600; color: var(--sky); letter-spacing: 0.5px; line-height: 1; }
  .person-role { font-size: 16px; font-weight: 500; margin-top: 6px; letter-spacing: 0.5px; }
  .rule { height: 1px; background: var(--rule); margin: 16px 0 18px; }

  .contact-row {
    display: flex; align-items: center; gap: 14px;
    font-family: "Montserrat", sans-serif; font-size: 21px; color: var(--white);
    margin-bottom: 12px; white-space: nowrap;
  }
  .contact-row svg { width: 26px; height: 26px; flex: none; fill: var(--sky); }

  .details { position: absolute; left: 460px; top: 30px; width: 350px; font-family: "Montserrat", sans-serif; color: var(--white); }
  .social { display: flex; align-items: center; justify-content: flex-end; gap: 10px; font-size: 15px; }
  .social-dot { width: 24px; height: 24px; border-radius: 50%; background: var(--sky); }
  .details .rule { margin: 10px 0 16px; }
  .address { line-height: 1.25; }
</style>
</head>
<body>
<main class="canvas">

  <section class="card card--front" aria-label="Business card front">
    <div class="brand">
      <div class="brand-mark"></div>
      <span class="brand-name">Brivoldex.com</span>
    </div>

    <div class="color-stripe"><span></span><span></span><span></span><span></span></div>

    <div class="front-panel">
      <div class="person">
        <p class="person-name">JOHN DOE</p>
        <p class="person-role">POSITION</p>
        <div class="rule"></div>
        <p class="contact-row">
          <svg viewBox="0 0 24 24" aria-hidden="true"><path d="M6.6 10.8a15.1 15.1 0 0 0 6.6 6.6l2.2-2.2a1 1 0 0 1 1-.25 11.4 11.4 0 0 0 3.6.57 1 1 0 0 1 1 1V20a1 1 0 0 1-1 1A17 17 0 0 1 3 4a1 1 0 0 1 1-1h3.5a1 1 0 0 1 1 1c0 1.25.2 2.45.57 3.570a1 1 0 0 1-.25 1z"/></svg>
          (000) 000 0000
        </p>
        <p class="contact-row">
          <svg viewBox="0 0 24 24" aria-hidden="true"><path d="M2 5h20v14H2z M4 7v.4l8 5.2 8-5.2V7z" fill-rule="evenodd"/></svg>
          email@company.com
        </p>
      </div>

      <div class="details">
        <div class="social"><span>@Brivoldex</span><span class="social-dot"></span></div>
        <div class="rule"></div>
        <p class="contact-row">
          <svg viewBox="0 0 24 24" aria-hidden="true"><path d="M12 2a10 10 0 1 0 0 20 10 10 0 0 0 0-20zm6.9 6h-3a15.7 15.7 0 0 0-1.3-3.9A8 8 0 0 1 18.9 8zM12 4c.8 1.2 1.5 2.5 1.9 4h-3.8c.4-1.5 1.1-2.8 1.9-4zM4.3 14a8 8 0 0 1 0-4h3.4a16.5 16.5 0 0 0 0 4zm.8 2h3a15.7 15.7 0 0 0 1.3 3.9A8 8 0 0 1 5.1 16zm3-8h-3a8 8 0 0 1 4.3-3.9A15.7 15.7 0 0 0 8.1 8zM12 20c-.8-1.2-1.5-2.5-1.9-4h3.8c-.4 1.5-1.1 2.8-1.9 4zm2.3-6H9.7a14.7 14.7 0 0 1 0-4h4.6a14.7 14.7 0 0 1 0 4zm.3 5.9c.6-1.2 1-2.5 1.300-3.9h3a8 8 0 0 1-4.3 3.9zm1.7-5.9a16.5 16.5 0 0 0 0-4h3.4a8 8 0 0 1 0 4z"/></svg>
          www.company.com
        </p>
        <div class="contact-row">
          <svg viewBox="0 0 24 24" aria-hidden="true"><path d="M12 2a7 7 0 0 0-7 7c0 5.2 7 13 7 13s7-7.8 7-13a7 7 0 0 0-7-7zm0 9.5a2.5 2.5 0 1 1 0-5 2.5 2.5 0 0 1 0 5z"/></svg>
          <p class="address">123 Name Street, 000<br>Your City, 00000-000</p>
        </div>
      </div>
    </div>
  </section>

  <section class="card card--back" aria-label="Business card back">
    <div class="brand">
      <div class="brand-mark"></div>
      <span class="brand-name">Brivoldex.com</span>
    </div>
    <div class="color-stripe"><span></span><span></span><span></span><span></span></div>
  </section>

</main>
</body>
</html>
```